2026 Company Line Card

We would like to redesign our current company line card. We send this printed flyer to prospective customers to introduce our company, the brands we represent, and our competitive advantages. Our website is www.valvorimsupply.com, and our phone number is (800) 312-4470. We're a specialty supplier for plumbing material, specifically water and life safety products. Our customers are mostly male, blue-collar contractors, ages 40-60. I have included a pdf of our current flyer and our high-resolution transparent logo. We would also like to highlight certain key points, which include:
Genuine OEM Parts
Technical Assistance from Repair Experts
Repair Information
1-2 day Delivery for the United States
Friendly & Knowledgeable Customer Service
The Largest Parts Inventory In The Nation
Testing Equipment
Full Service Gauge Calibration and Repair

```html
<!DOCTYPE html>
<html lang="en">
<head>
<meta charset="utf-8">
<title>Valvorim Supply Company – Line Card</title>
<link rel="stylesheet" href="https://fonts.googleapis.com/css2?family=Montserrat:ital,wght@0,600;0,700;0,800;1,700;1,800&family=Open+Sans:wght@500&display=swap">
<style>
  :root {
    --blue: #1c55a6;
    --blue-deep: #184b95;
    --red: #e8363f;
    --ink: #1d1d1f;
    --sky: #cddff3;
    --white: #ffffff;
    --divider: #c9c9c9;
  }
  * { box-sizing: border-box; margin: 0; padding: 0; }
  html, body { width: 720px; height: 1200px; overflow: hidden; background: #f2f2f2; }
  .line-card {
    position: relative; width: 720px; height: 1200px; overflow: hidden;
    background: linear-gradient(100deg, var(--white) 42%, var(--sky) 100%);
    font-family: "Montserrat", sans-serif;
  }
  .hero-photo {
    position: absolute; left: 420px; top: 18px; width: 300px; height: 560px;
    background: linear-gradient(180deg, rgba(205,223,243,0) 0%, #9cbde6 30%, #3f7fcf 65%, #2a66b8 100%);
  }
  .brand { position: absolute; left: 36px; top: 58px; display: flex; align-items: center; gap: 14px; }
  .brand-dot { width: 34px; height: 34px; border-radius: 50%; background: var(--red); flex: none; }
  .brand-name { font-family: "Open Sans", sans-serif; font-weight: 500; font-size: 33px; line-height: 40px; color: var(--blue); letter-spacing: -.3px; }
  .lead-in { position: absolute; left: 36px; top: 178px; font-weight: 800; font-size: 16px; color: var(--ink); }
  .headline-list { position: absolute; left: 36px; top: 220px; list-style: none; }
  .headline-list li { display: flex; align-items: center; gap: 12px; font-weight: 800; font-size: 24px; color: var(--red); line-height: 36px; letter-spacing: .2px; }
  .headline-list svg { width: 19px; height: 19px; flex: none; }
  .product-photo {
    position: absolute; left: 36px; top: 348px; width: 340px; height: 250px;
    background: linear-gradient(135deg, #9a9a8c 0%, #6f6f64 55%, #d9d9d2 100%);
    border-radius: 18px;
  }
  .band { position: absolute; left: 0; top: 0; width: 720px; height: 1200px; }
  .advantage-list { position: absolute; left: 44px; top: 664px; list-style: none; color: var(--white); }
  .advantage-list li { display: flex; gap: 12px; font-weight: 700; font-size: 15px; line-height: 18px; margin-bottom: 13px; }
  .advantage-list svg { width: 14px; height: 14px; flex: none; margin-top: 2px; }
  .contact-bar {
    position: absolute; left: 0; top: 1003px; width: 720px; height: 65px; background: var(--red);
    display: flex; align-items: center; justify-content: center; gap: 30px;
    color: var(--white); font-weight: 800; font-style: italic; font-size: 25px;
  }
  .contact-item { display: flex; align-items: center; gap: 10px; white-space: nowrap; }
  .contact-item svg { width: 22px; height: 22px; }
  .partner-strip {
    position: absolute; left: 0; top: 1068px; width: 720px; height: 132px; background: var(--white);
    padding: 12px 28px;
  }
  .partner-grid {
    width: 664px; height: 108px;
    display: grid; grid-template-columns: repeat(7, 1fr); grid-template-rows: 1fr 1fr;
  }
  .partner {
    display: flex; align-items: center; justify-content: center;
    font-weight: 700; font-size: 13px; color: var(--blue-deep); text-align: center; white-space: nowrap;
    border-right: 1px solid var(--divider);
  }
  .partner:nth-child(7n) { border-right: none; }
</style>
</head>
<body>
<main class="line-card">
  <div class="hero-photo" role="img" aria-label="Photo: smiling technician in a blue work shirt holding a pipe wrench"></div>

  <header class="brand">
    <span class="brand-dot"></span>
    <span class="brand-name">Valvorim Supply Company</span>
  </header>

  <p class="lead-in">THE NATION'S LEADING SOURCE FOR:</p>
  <ul class="headline-list">
    <li><svg viewBox="0 0 20 20"><circle cx="10" cy="10" r="10" fill="#1c55a6"/><path d="M5.5 10.2l3 3 6-6" stroke="#fff" stroke-width="2.4" fill="none"/></svg>GENUINE OEM PARTS</li>
    <li><svg viewBox="0 0 20 20"><circle cx="10" cy="10" r="10" fill="#1c55a6"/><path d="M5.5 10.2l3 3 6-6" stroke="#fff" stroke-width="2.4" fill="none"/></svg>REPAIR INFORMATION</li>
    <li><svg viewBox="0 0 20 20"><circle cx="10" cy="10" r="10" fill="#1c55a6"/><path d="M5.5 10.2l3 3 6-6" stroke="#fff" stroke-width="2.4" fill="none"/></svg>TECHNICAL ASSISTANCE</li>
  </ul>

  <div class="product-photo" role="img" aria-label="Photo: backflow test kit case with differential pressure gauge and coloured hoses"></div>

  <svg class="band" viewBox="0 0 720 1200">
    <polygon points="0,632 720,520 720,532 0,644" fill="#e8363f"/>
    <polygon points="0,644 720,532 720,1003 0,1003" fill="#1c55a6"/>
    <g stroke="#e8363f" stroke-width="6">
      <g role="img" aria-label="Photo: red backflow preventer assembly installed outdoors">
        <polygon points="542,490 611,530 611,610 542,650 473,610 473,530" fill="#b8473f"/>
      </g>
      <g role="img" aria-label="Photo: hand reaching into an open valve body">
        <polygon points="465,620 534,660 534,740 465,780 396,740 396,660" fill="#a79a90"/>
      </g>
      <g role="img" aria-label="Photo: check valve spring assembly being removed from a valve">
        <polygon points="619,620 688,660 688,740 619,780 550,740 550,660" fill="#c89a90"/>
      </g>
      <g role="img" aria-label="Photo: replacement check valve parts and rubber seals">
        <polygon points="542,750 611,790 611,870 542,910 473,870 473,790" fill="#eeeeee"/>
      </g>
    </g>
  </svg>

  <ul class="advantage-list">
    <li><svg viewBox="0 0 14 14"><path d="M2 7.5l3 3 7-7" stroke="#fff" stroke-width="2" fill="none"/></svg>Genuine OEM Parts</li>
    <li><svg viewBox="0 0 14 14"><path d="M2 7.5l3 3 7-7" stroke="#fff" stroke-width="2" fill="none"/></svg><span>Technical Assistance from<br>Repair Experts</span></li>
    <li><svg viewBox="0 0 14 14"><path d="M2 7.5l3 3 7-7" stroke="#fff" stroke-width="2" fill="none"/></svg>Repair Information</li>
    <li><svg viewBox="0 0 14 14"><path d="M2 7.5l3 3 7-7" stroke="#fff" stroke-width="2" fill="none"/></svg>1-2 day Delivery for the United States</li>
    <li><svg viewBox="0 0 14 14"><path d="M2 7.5l3 3 7-7" stroke="#fff" stroke-width="2" fill="none"/></svg><span>Friendly &amp; Knowledgeable<br>Customer Service</span></li>
    <li><svg viewBox="0 0 14 14"><path d="M2 7.5l3 3 7-7" stroke="#fff" stroke-width="2" fill="none"/></svg><span>The Largest Parts Inventory<br>In The Nation</span></li>
    <li><svg viewBox="0 0 14 14"><path d="M2 7.5l3 3 7-7" stroke="#fff" stroke-width="2" fill="none"/></svg>Testing Equipment</li>
    <li><svg viewBox="0 0 14 14"><path d="M2 7.5l3 3 7-7" stroke="#fff" stroke-width="2" fill="none"/></svg><span>Full Service Gauge Calibration<br>and Repair</span></li>
  </ul>

  <footer class="contact-bar">
    <span class="contact-item">
      <svg viewBox="0 0 24 24"><rect x="2" y="5" width="20" height="14" fill="none" stroke="#fff" stroke-width="2"/><path d="M2 5l10 8 10-8M2 19l7-7M22 19l-7-7" stroke="#fff" stroke-width="2" fill="none"/></svg>
      www.valvorimsupply.com
    </span>
    <span class="contact-item">
      <svg viewBox="0 0 24 24"><path d="M6 3l3 5-2 2c1 3 4 6 7 7l2-2 5 3-2 4C10 22 2 14 2 5z" fill="none" stroke="#fff" stroke-width="2"/></svg>
      (800) 312-4470
    </span>
  </footer>

  <section class="partner-strip" aria-label="Brands we represent">
    <div class="partner-grid">
      <span class="partner">Corvane</span>
      <span class="partner">Halden</span>
      <span class="partner">Ridgeline</span>
      <span class="partner">Norvik</span>
      <span class="partner">Tessar</span>
      <span class="partner">Brandt</span>
      <span class="partner">Stonewell</span>
      <span class="partner">Kellam</span>
      <span class="partner">Aldrow</span>
      <span class="partner">Warmcase</span>
      <span class="partner">Prairie Gauge</span>
      <span class="partner">Guardlid</span>
      <span class="partner">Merrow</span>
      <span class="partner">Oakhurst</span>
    </div>
  </section>
</main>
</body>
</html>
```